Business Card Design & logo

Residential building renovation and maintenance work.
All carpentry and joinery needs.
Laying solid timber and floating floors.
Kitchen and bathroom makeovers and modifications.
Interior fitouts,
small job specialist. tiling, plastering, painting,

I would like a silver background. With the use of different shades of grey, rustic orange, black and white.
I do not want pictures of hammers, chisels etc. I am looking for a logo to be incorporated into the card.

Carpentry

Contact Information for Business Card

BTQ Renovations and Maintenance
Lewis Tolbane
0471852036
info@btqfixes.com.au
btqfixes.com.au

```html
<!DOCTYPE html>
<html lang="en">
<head>
<meta charset="UTF-8">
<title>BTQ Renovations and Maintenance – Business Card</title>
<link href="https://fonts.googleapis.com/css2?family=Raleway:wght@400;500;600&display=swap" rel="stylesheet">
<style>
  :root {
    --stage: #1d1e20;
    --card-front: #2f3034;
    --card-back: #333438;
    --orange: #f08a24;
    --grey-light: #c9cacc;
    --white: #ffffff;
  }
  * { margin: 0; padding: 0; box-sizing: border-box; }
  html, body {
    width: 1200px;
    height: 900px;
    overflow: hidden;
    background: var(--stage);
    font-family: "Raleway", sans-serif;
  }
  .stage { position: relative; width: 1200px; height: 900px; }
  .card {
    position: absolute;
    left: 331px;
    width: 542px;
    height: 315px;
    border-radius: 14px;
  }
  .card--front { top: 121px; background: var(--card-front); }
  .card--back { top: 487px; background: var(--card-back); }

  .brand {
    position: absolute;
    display: flex;
    flex-direction: column;
    align-items: center;
    text-align: center;
  }
  .brand__mark { display: block; }
  .brand__name {
    font-weight: 500;
    letter-spacing: 0.06em;
    line-height: 1.25;
    text-transform: uppercase;
  }
  .card--front .brand { left: 28px; top: 108px; width: 240px; }
  .card--front .brand__mark { width: 40px; height: 40px; background: var(--orange); margin-bottom: 16px; }
  .card--front .brand__name { color: var(--orange); font-size: 17px; }

  .card--back .brand { left: 0; right: 0; top: 82px; }
  .card--back .brand__mark { width: 60px; height: 60px; background: var(--white); margin-bottom: 22px; }
  .card--back .brand__name { color: var(--white); font-size: 26px; }

  .contact { position: absolute; left: 313px; top: 114px; }
  .contact__name { color: var(--orange); font-size: 26px; font-weight: 500; line-height: 1.1; }
  .contact__role { color: var(--grey-light); font-size: 16px; margin-top: 2px; }
  .contact__details { margin-top: 22px; color: var(--white); font-size: 14px; line-height: 1.35; padding-left: 2px; }
</style>
</head>
<body>
  <main class="stage">
    <section class="card card--front">
      <div class="brand">
        <span class="brand__mark"></span>
        <p class="brand__name">BTQ Renovations<br>&amp; Maintenance</p>
      </div>
      <div class="contact">
        <p class="contact__name">Lewis Tolbane</p>
        <p class="contact__role">Managing Director</p>
        <div class="contact__details">
          <p>info@btqfixes.com.au</p>
          <p>0471 852 036</p>
        </div>
      </div>
    </section>

    <section class="card card--back">
      <div class="brand">
        <span class="brand__mark"></span>
        <p class="brand__name">BTQ Renovations<br>&amp; Maintenance</p>
      </div>
    </section>
  </main>
</body>
</html>
```